Need Bus charter business website,

I am starting a bus charter business in the near future. I am based in Geelong, Victoria in Australia. I will have a 25 or 28 seater bus that will be used to take people on charted trips. Whether they be to birthday parties, weddings, sporting events, corporate events, mystery trips, going down the Great Ocean Road, or anywhere someone wants. As for colour scheme, I'm leaning towards something blue and grey, but open to anything really that catches my eye. I played around with a basic web design program and made a basic site which I uploaded ( www.kelvomtravel.com.au) It has things which I wanted to include such as, services I will provide, trip information, contact form etc.

I don't mind if the layout is completely different to my site as it was only a template that was included in the program I used. I would like the overall design to be relatively fluid, not having to back-track a lot to navigate the site.

```html
<!DOCTYPE html>
<html lang="en">
<head>
<meta charset="utf-8">
<title>Bayline Bus Tours</title>
<link href="https://fonts.googleapis.com/css2?family=Source+Sans+3:ital,wght@0,400;0,600;1,400&family=Vollkorn:wght@400&display=swap" rel="stylesheet">
<style>
:root{
  --blue:#2f6a99;
  --blue-light:#4a87bf;
  --blue-dark:#1f4e7a;
  --text:#555;
  --heading:#333;
  --line:#ddd;
  --panel:#f6f6f6;
  --footer:#474747;
}
*{box-sizing:border-box;margin:0;padding:0}
html,body{width:1003px;height:1200px;overflow:hidden;background:#fff}
body{font-family:"Source Sans 3",sans-serif;color:var(--text);position:relative}
.abs{position:absolute}
.brand{left:109px;top:24px;font-family:"Vollkorn",serif;font-size:28px;color:#111;letter-spacing:.5px}
.search{left:766px;top:33px;width:127px;height:25px;border:1px solid #ccc;border-radius:2px;background:#fff}
.search svg{position:absolute;right:6px;top:6px}
.search .divider{position:absolute;right:27px;top:4px;width:1px;height:16px;background:#ddd}
.nav{left:109px;top:89px;width:786px;height:47px;background:var(--blue)}
.nav a{color:#fff;text-decoration:none;font-size:12px;text-transform:uppercase;position:absolute;top:15px}
.nav .active-bg{position:absolute;left:0;top:0;width:135px;height:47px;background:var(--blue-light)}
.hero{left:0;top:136px;width:1003px;height:416px;background:linear-gradient(180deg,#cfc9c3 0%,#a8a6a6 45%,#8c8a8c 70%,#c9c3bf 100%)}
.arrow{position:absolute;top:337px;width:42px;height:42px;border:2px solid #fff;border-radius:50%}
.arrow svg{position:absolute;left:13px;top:13px}
h1.welcome{left:110px;top:600px;font-family:"Vollkorn",serif;font-weight:400;font-size:20px;color:var(--heading)}
.welcome span{color:var(--blue)}
.intro{left:110px;top:644px;width:577px;font-size:11.3px;line-height:21px}
.btn{display:inline-block;background:var(--blue);color:#fff;font-size:11.5px;text-align:center;border-radius:1px}
.btn-intro{left:111px;top:722px;width:93px;height:30px;line-height:30px}
.team-photo{left:710px;top:613px;width:185px;height:125px;border:1px solid #ddd;background:linear-gradient(90deg,#e9edf1,#f4f4f3 45%,#dfe3e8)}
.card{top:799px;width:241px;height:274px;border:1px solid var(--line);background:var(--panel)}
.card h2{font-family:"Vollkorn",serif;font-weight:400;font-size:20px;color:var(--heading);position:absolute;left:20px;top:18px}
.card h2 span{color:var(--blue)}
.about p{position:absolute;left:20px;top:62px;width:205px;font-size:11px;line-height:21px}
.about .btn{position:absolute;left:20px;top:224px;width:91px;height:29px;line-height:29px}
.services ul{list-style:none;position:absolute;left:14px;top:64px;width:210px}
.services li{font-size:11px;height:26px;line-height:22px;border-bottom:1px dashed #ddd;padding-left:23px;position:relative}
.services li:last-child{border-bottom:none}
.services li::before{content:"";position:absolute;left:9px;top:9px;width:5px;height:5px;border-radius:50%;background:var(--blue)}
.book{background:linear-gradient(180deg,#3f7db6,#2e669b);border-color:#2e669b;color:#fff;text-align:center}
.book h2{color:#fff;left:0;width:100%}
.book p{position:absolute;left:18px;top:58px;width:205px;font-size:11px;line-height:20px}
.field{position:absolute;left:21px;width:197px;height:31px;background:#fff;font-style:italic;font-size:11px;color:#999;text-align:left;padding-left:33px;line-height:31px}
.field svg{position:absolute;left:14px;top:10px}
.book .submit{position:absolute;left:147px;top:231px;width:71px;height:27px;line-height:27px;background:var(--blue-dark);font-size:11.5px;font-weight:600}
.footer{left:0;top:1123px;width:1003px;height:77px;background:var(--footer)}
.copy{position:absolute;left:140px;top:34px;font-size:11px;color:#ddd}
.social{position:absolute;top:26px;width:30px;height:30px;border:2px solid #bbb;border-radius:50%;background:#5a5a5a}
</style>
</head>
<body>
<div class="abs brand">Bayline Bus Tours</div>
<div class="abs search">
  <span class="divider"></span>
  <svg width="11" height="11" viewBox="0 0 11 11"><circle cx="4.5" cy="4.5" r="3.5" fill="none" stroke="#999" stroke-width="1.5"/><line x1="7" y1="7" x2="10" y2="10" stroke="#999" stroke-width="1.6"/></svg>
</div>

<nav class="abs nav">
  <span class="active-bg"></span>
  <a style="left:26px">Bayline Bus Tours</a>
  <a style="left:169px">About Us</a>
  <a style="left:268px">Services</a>
  <a style="left:365px">Trips on Offers</a>
  <a style="left:502px">Book a Trip</a>
  <a style="left:612px">Contact Us</a>
</nav>

<div class="abs hero" role="img" aria-label="Large white coach bus speeding past with motion blur"></div>
<span class="abs arrow" style="left:50px"><svg width="12" height="12" viewBox="0 0 12 12"><polyline points="8,2 4,6 8,10" fill="none" stroke="#fff" stroke-width="2.2"/></svg></span>
<span class="abs arrow" style="left:909px"><svg width="12" height="12" viewBox="0 0 12 12"><polyline points="4,2 8,6 4,10" fill="none" stroke="#fff" stroke-width="2.2"/></svg></span>

<h1 class="abs welcome">Welcome to Our Website <span>Mainpage...</span></h1>
<p class="abs intro">We are an accredited bus company that operates bus trip and charter work in the Geelong area. We offer a range of services, from day trips down the Great Ocean Road, to transport for wedding guests, Buck’s and Hen’s nights or school trips. We are an accredited bus company that operates bus trip.</p>
<a class="abs btn btn-intro">Read More</a>
<div class="abs team-photo" role="img" aria-label="Smiling businesswoman with arms crossed in front of two colleagues in an office"></div>

<section class="abs card about" style="left:110px">
  <h2>About <span>us</span></h2>
  <p>Bayline Bus Tours is a family run business. We pride ourselves on providing great service and value for money. We know and love the Geelong region and want to explore more of it with you. Bayline Bus Tours is a family run business. We pride ourselves on providing.</p>
  <a class="btn">Read More</a>
</section>

<section class="abs card services" style="left:381px">
  <h2>Services</h2>
  <ul>
    <li>Weddings</li><li>Buck’s Party</li><li>Hens Party</li><li>Winery Party</li>
    <li>Birthdays</li><li>Corporate Events</li><li>Sporting</li><li>Mystery Trips</li>
  </ul>
</section>

<section class="abs card book" style="left:653px">
  <h2>Want to book a trip?</h2>
  <p>Check out our trips we are currently offering here or if you have an idea or location in mind, contact us here and we’ll do our best to make it happen.</p>
  <div class="field" style="top:153px"><svg width="11" height="11" viewBox="0 0 11 11"><circle cx="5.5" cy="3" r="2.7" fill="#999"/><path d="M0.5 11 Q5.5 4 10.5 11Z" fill="#999"/></svg>Enter your Name...</div>
  <div class="field" style="top:191px"><svg width="12" height="9" viewBox="0 0 12 9"><rect x="0.5" y="0.5" width="11" height="8" fill="none" stroke="#999"/><polyline points="0.5,0.5 6,5 11.5,0.5" fill="none" stroke="#999"/></svg>Enter your Email...</div>
  <a class="btn submit">Submit</a>
</section>

<footer class="abs footer">
  <p class="copy">Copyright ©2014 Yoursite All Rights Reserved.</p>
  <span class="social" style="left:782px" aria-label="Social link 1"></span>
  <span class="social" style="left:822px" aria-label="Social link 2"></span>
  <span class="social" style="left:862px" aria-label="Social link 3"></span>
</footer>
</body>
</html>
```